Company Mission & Values Poster

I'd like an A2 Portrait Poster displaying our company's Mission & Values.
See our website for our logo, fonts, mission & values.
https://talvendo.com.au/

Our Mission: Creating homes for abundant life
Values: Love, Thinking, Team, Zoe.

Some ideas to consider:
Mission as the Headline then
A logo for each of the 4 Values and the words

Target Market(s)

Myself & my team

Industry/Entity Type

Real Estate

Font styles to use
Other font styles liked:
• Company fonts as seen on our website

```html
<!DOCTYPE html>
<html lang="en">
<head>
<meta charset="utf-8">
<title>Talvendo – Mission &amp; Values Posters</title>
<link rel="stylesheet" href="https://fonts.googleapis.com/css2?family=Source+Serif+4:opsz,wght@8..60,400;8..60,500&family=Marcellus+SC&display=swap">
<style>
  :root {
    --forest: #0e372f;
    --paper: #ffffff;
    --backdrop: #e6e6e6;
  }
  * { margin: 0; padding: 0; box-sizing: border-box; }
  html, body { width: 1200px; height: 1200px; overflow: hidden; background: var(--backdrop); }
  body { position: relative; font-family: "Source Serif 4", Georgia, serif; color: var(--forest); }

  .poster {
    position: absolute;
    width: 356px;
    height: 506px;
    background: var(--paper);
    overflow: hidden;
    box-shadow: 4px 6px 10px rgba(0,0,0,0.28);
  }
  .poster--curve-foot { left: 212px; top: 77px; }
  .poster--band-head  { left: 613px; top: 77px; width: 358px; }
  .poster--arc-frame  { left: 217px; top: 624px; width: 353px; background: var(--forest); }
  .poster--small-caps { left: 613px; top: 624px; width: 358px; font-family: "Marcellus SC", Georgia, serif; }

  .backdrop-shape { position: absolute; inset: 0; width: 100%; height: 100%; }

  .label, .headline, .wordmark, .values { position: absolute; left: 0; width: 100%; text-align: center; }
  .label { font-size: 17px; line-height: 20px; }
  .headline { font-size: 24px; line-height: 30px; font-weight: 400; }
  .headline--light { color: var(--paper); font-size: 22px; line-height: 28px; }

  .rule {
    position: absolute; left: 40px; width: 278px; height: 2px;
    background: linear-gradient(90deg, transparent, var(--forest) 12%, var(--forest) 88%, transparent);
    border-radius: 50%;
  }

  .band { position: absolute; left: 0; width: 100%; background: var(--forest); }

  .values { list-style: none; }
  .value { height: 54px; display: flex; flex-direction: column; align-items: center; }
  .value__mark { width: 9px; height: 9px; border: 1.5px solid var(--forest); border-radius: 50%; }
  .value__word { font-size: 23px; line-height: 1; margin-top: 8px; }

  .wordmark {
    display: flex; align-items: center; justify-content: center; gap: 10px;
    font-size: 24px; line-height: 1; letter-spacing: 0.2em; font-weight: 400;
  }
  .wordmark__dot { width: 16px; height: 16px; border-radius: 50%; background: currentColor; }
  .wordmark--light { color: var(--paper); }
  .wordmark--large { font-size: 30px; }
  .wordmark--large .wordmark__dot { width: 20px; height: 20px; }
</style>
</head>
<body>

  <!-- Variant 1: rules around headline, curved green foot -->
  <section class="poster poster--curve-foot">
    <svg class="backdrop-shape" viewBox="0 0 356 506" preserveAspectRatio="none" aria-hidden="true">
      <path d="M0,390 C70,425 140,438 200,437 C260,436 310,424 356,410 V506 H0 Z" fill="var(--forest)"/>
    </svg>
    <p class="label" style="top:49px">Our Mission:</p>
    <div class="rule" style="top:74px"></div>
    <h1 class="headline" style="top:79px">Creating homes for<br>abundant life</h1>
    <div class="rule" style="top:143px"></div>
    <ul class="values" style="top:176px">
      <li class="value"><span class="value__mark"></span><span class="value__word">Love</span></li>
      <li class="value"><span class="value__mark"></span><span class="value__word">Thinking</span></li>
      <li class="value"><span class="value__mark"></span><span class="value__word">Team</span></li>
      <li class="value"><span class="value__mark"></span><span class="value__word">Zoe</span></li>
    </ul>
    <div class="wordmark wordmark--light" style="top:459px"><span class="wordmark__dot"></span>TALVENDO</div>
  </section>

  <!-- Variant 2: green headline band, rule above wordmark -->
  <section class="poster poster--band-head">
    <p class="label" style="top:59px">Our Mission:</p>
    <div class="band" style="top:82px; height:66px"></div>
    <h1 class="headline headline--light" style="top:87px">Creating homes for<br>abundant life</h1>
    <ul class="values" style="top:166px">
      <li class="value"><span class="value__mark"></span><span class="value__word">Love</span></li>
      <li class="value"><span class="value__mark"></span><span class="value__word">Thinking</span></li>
      <li class="value"><span class="value__mark"></span><span class="value__word">Team</span></li>
      <li class="value"><span class="value__mark"></span><span class="value__word">Zoe</span></li>
    </ul>
    <div class="rule" style="top:424px; left:41px; width:276px"></div>
    <div class="wordmark wordmark--large" style="top:444px">
      <span class="wordmark__dot"></span>TALVENDO</div>
  </section>

  <!-- Variant 3: green frame with large white arc -->
  <section class="poster poster--arc-frame">
    <svg class="backdrop-shape" viewBox="0 0 353 506" preserveAspectRatio="none" aria-hidden="true">
      <path d="M89,0 H353 V414 C310,432 275,437 243,437 C130,437 40,370 0,288 V185 C20,110 50,45 89,0 Z" fill="var(--paper)"/>
    </svg>
    <p class="label" style="top:49px">Our Mission:</p>
    <h1 class="headline" style="top:79px">Creating homes for<br>abundant life</h1>
    <ul class="values" style="top:176px">
      <li class="value"><span class="value__mark"></span><span class="value__word">Love</span></li>
      <li class="value"><span class="value__mark"></span><span class="value__word">Thinking</span></li>
      <li class="value"><span class="value__mark"></span><span class="value__word">Team</span></li>
      <li class="value"><span class="value__mark"></span><span class="value__word">Zoe</span></li>
    </ul>
    <div class="wordmark wordmark--light" style="top:462px; left:29px; width:auto; font-size:21px">
      <span class="wordmark__dot" style="width:14px;height:14px"></span>TALVENDO</div>
  </section>

  <!-- Variant 4: small caps with headline band and footer band -->
  <section class="poster poster--small-caps">
    <p class="label" style="top:51px">Our Mission:</p>
    <div class="band" style="top:75px; height:65px"></div>
    <h1 class="headline headline--light" style="top:79px; letter-spacing:0.05em">Creating homes for<br>abundant life</h1>
    <ul class="values" style="top:158px">
      <li class="value"><span class="value__mark"></span><span class="value__word">Love</span></li>
      <li class="value"><span class="value__mark"></span><span class="value__word">Thinking</span></li>
      <li class="value"><span class="value__mark"></span><span class="value__word">Team</span></li>
      <li class="value"><span class="value__mark"></span><span class="value__word">Zoe</span></li>
    </ul>
    <div class="band" style="top:408px; height:66px"></div>
    <div class="wordmark wordmark--light wordmark--large" style="top:426px; font-family:'Source Serif 4', Georgia, serif">
      <span class="wordmark__dot"></span>TALVENDO</div>
  </section>

</body>
</html>
```